Humorous Book by Comedian Needs E-book Cover

My book 'A Kettle on the Porch' is on Leafpad but I want a better cover designed. Cover needs my photo on it. My name is the most important text (because I have an existing audience.)

Text elements:
Author: Dorvel Pim
Title: A Kettle on the Porch
Subtitle: Tenth Anniversary Edition
Review Quote: 'All of his columns are amusing. The best are masterpieces.' Harbour Ledger

Above my name it should say: Collected Humour From NZ's Award-Winning Comedian

Here's the present version (which is why I want an improved version!)
http://www.brightmart-example.com/A-Kettle-Porch-Anniversary-Edition-ebook/dp/Q77TX2M904

Book covers I admire:

http://www.brightmart-example.co.uk/Why-The-Fern-Odile-Brask-ebook/dp/Q3318ZR7LN/ref=tmm_kin_title_0

http://www.brightmart-example.com/Gravelhat-Mira-Dunst-ebook/dp/Q691PLE583/ref=tmm_kin_title_0

http://www.brightmart-example.co.uk/Why-Keep-Lantern-Rex-Palfrey-ebook/dp/Q58JN3TQ7V

Leafpad covers need to work as thumbnails, as well as on small device screens.

This cover is for Brightmart Leafpad. Tech specs are on Leafpad Direct Publishing page. Dimensions: Requirements for the size of your cover art have an ideal height/width ratio of 1.6, this means: • A minimum of 625 pixels on the shortest side and 1000 pixels on the longest side • For best quality, your image would be 2820 pixels on the shortest side and 4500 pixels on the longest side

Dimensions Requirements for the size of your cover art have an ideal height/width ratio of 1.6, this means: • A minimum of 625 pixels on the shortest side and 1000 pixels on the longest side • For best quality, your image would be 2820 pixels on the shortest side and 4500 pixels on the longest side

Comedian

```html
<!DOCTYPE html>
<html lang="en">
<head>
<meta charset="utf-8">
<title>A Kettle on the Porch — Dorvel Pim</title>
<link rel="stylesheet" href="https://fonts.googleapis.com/css2?family=Kaushan+Script&family=Open+Sans:wght@700&family=Almendra:ital,wght@1,700&family=Libre+Baskerville:ital@1&family=Cinzel:wght@700&display=swap">
<style>
  :root{
    --bg:#d4d7de;
    --rust:#b4442a;
    --brown:#8a4a22;
    --stripe-dark:#3a3838;
    --stripe-red:#c2452b;
    --ink:#222;
    --gold:#d9a53a;
    --gold-deep:#a8741c;
    --gold-light:#f4d27a;
    --cream:#ece4cf;
  }
  *{margin:0;padding:0;box-sizing:border-box}
  html,body{width:800px;height:1200px;overflow:hidden;background:var(--bg)}
  .cover{position:relative;width:800px;height:1200px;background:var(--bg);overflow:hidden}
  .cover-art{position:absolute;inset:0}
  .author-name{
    position:absolute;top:8px;left:0;width:800px;text-align:center;
    font-family:"Kaushan Script",cursive;font-weight:400;font-size:138px;color:var(--rust);line-height:1.1;letter-spacing:2px;
  }
  .tagline{
    position:absolute;top:226px;left:0;width:800px;text-align:center;padding-left:70px;
    font-family:"Open Sans",sans-serif;font-weight:700;font-size:18px;color:var(--ink);letter-spacing:-.2px;
  }
  .edition-seal{position:absolute;left:42px;top:265px;width:230px;height:230px}
  .edition-text{
    position:absolute;left:42px;top:265px;width:230px;height:230px;
    display:flex;flex-direction:column;align-items:center;justify-content:center;
    font-family:"Cinzel",serif;font-weight:700;color:#4a2a10;text-align:center;line-height:1.05;
  }
  .edition-text .big{font-size:38px}
  .edition-text .small{font-size:20px}
  .review{
    position:absolute;left:528px;top:283px;width:240px;
    font-family:"Libre Baskerville",serif;font-style:italic;font-size:16px;color:var(--ink);line-height:1.4;
  }
  .review-source{display:block;text-align:right;margin-top:8px;font-style:normal;font-size:16px}
  .book-title{
    position:absolute;left:0;top:858px;width:800px;text-align:center;
    font-family:"Almendra",serif;font-style:italic;font-weight:700;font-size:124px;line-height:1.08;
    color:var(--rust);
  }
</style>
</head>
<body>
<div class="cover">
  <svg class="cover-art" width="800" height="1200" viewBox="0 0 800 1200">
    <defs>
      <linearGradient id="portraitTone" x1="0" y1="0" x2="0" y2="1">
        <stop offset="0" stop-color="#d4d7de" stop-opacity="0"/>
        <stop offset=".35" stop-color="#e6e2d6"/>
        <stop offset="1" stop-color="var(--cream)"/>
      </linearGradient>
      <radialGradient id="sealFace" cx=".45" cy=".4" r=".7">
        <stop offset="0" stop-color="var(--gold-light)"/>
        <stop offset="1" stop-color="var(--gold)"/>
      </radialGradient>
    </defs>
    <path class="swoop-band" fill="var(--brown)" d="M0,500 Q150,760 400,800 Q650,760 800,480 L800,680 Q400,930 0,700 Z"/>
    <path class="author-portrait" role="img" aria-label="Photo of the author in a cream dinner jacket and bow tie" fill="url(#portraitTone)"
      d="M300,240 Q400,215 480,250 L500,420 Q640,450 660,560 L690,800 Q400,830 190,800 L200,560 Q220,450 320,420 Z"/>
    <path class="swoop-stripe-dark" fill="none" stroke="var(--stripe-dark)" stroke-width="12" d="M0,700 Q400,930 800,680"/>
    <path class="swoop-stripe-red" fill="none" stroke="var(--stripe-red)" stroke-width="16" d="M0,718 Q400,950 800,698"/>
  </svg>

  <h1 class="author-name">Dorvel Pim</h1>
  <p class="tagline">Collected Humour From NZ's Award-Winning Comedian</p>

  <svg class="edition-seal" viewBox="0 0 230 230" aria-hidden="true">
    <circle cx="115" cy="115" r="113" fill="var(--gold-deep)"/>
    <circle cx="115" cy="115" r="102" fill="url(#sealFace)"/>
    <circle cx="115" cy="115" r="90" fill="none" stroke="var(--gold-deep)" stroke-width="2"/>
  </svg>
  <div class="edition-text">
    <span class="big">Tenth</span>
    <span class="small">Anniversary</span>
    <span class="big">Edition</span>
  </div>

  <blockquote class="review">‘All of his columns are amusing. The best are masterpieces.’
    <cite class="review-source">Harbour Ledger</cite>
  </blockquote>

  <h2 class="book-title">A Kettle on the<br>Porch</h2>
</div>
</body>
</html>
```